One Page Website for Personal Trainer in London

I have a logo and need a one page website designed around my branding. I am a freelance Personal Trainer based in London specialising in bodyweight training for men and women. I would like the site to be modern and clean but not overtly urban in design.
I need the following headings:
About Me
My Services
Events
Blog
I don't need them to be seperate pages but if they can link to further down the page that would be great.
Industry/Entity Type
Personal Trainer
Coding
Coded - Design and coding required
Number of Pages Required
1 page
Requirements
Must have
- I need the following headings:
- About Me
- My Services
- Events
- Blog
- mobile friendly formatting
- health and fitness related photography
- Colour scheme in keeping with my existing logo

```html
<!DOCTYPE html>
<html lang="en">
<head>
<meta charset="utf-8">
<title>Marlow Hayes – Personal Training</title>
<link href="https://fonts.googleapis.com/css2?family=Baloo+2:wght@700;800&family=Libre+Baskerville:wght@700&family=Open+Sans:wght@400;600;700&display=swap" rel="stylesheet">
<style>
:root{
  --orange:#f7941d;
  --orange-dark:#e07d0a;
  --ink:#222222;
  --text:#333333;
  --muted:#555555;
  --hero-bg:#f3f3f3;
  --section-grey:#f2f2f2;
  --cream:#fdf1e0;
  --footer:#000000;
  --footer-text:#cfcfcf;
  --white:#ffffff;
}
*{box-sizing:border-box;margin:0;padding:0}
html,body{width:1200px;height:3734px;overflow:hidden}
body{position:relative;background:var(--white);font-family:"Open Sans",Arial,sans-serif;color:var(--text)}
.abs{position:absolute}
a{color:inherit;text-decoration:none}

/* header */
.site-header{left:0;top:0;width:1200px;height:112px;background:var(--white)}
.brand{left:72px;top:26px;display:flex;align-items:center;gap:10px}
.brand-mark{width:34px;height:34px;border-radius:50%;background:var(--orange)}
.brand-name{font-weight:700;font-size:24px;color:var(--orange)}
.top-contact{right:72px;top:22px;display:flex;gap:28px;font-size:12px;color:var(--text);align-items:center}
.top-contact span{display:flex;align-items:center;gap:8px}
.main-nav{right:150px;top:78px;display:flex;gap:56px;font-size:12px;font-weight:700;color:var(--ink);letter-spacing:.5px}
.search-btn{left:1090px;top:68px;width:38px;height:38px;border-radius:50%;background:var(--orange);display:flex;align-items:center;justify-content:center}

/* hero */
.hero{left:0;top:112px;width:1200px;height:480px;background:var(--hero-bg)}
.hero-title{left:150px;top:180px;font-family:"Baloo 2",sans-serif;font-weight:800;font-size:108px;line-height:1;color:var(--ink)}
.hero-title em{font-style:normal;color:var(--orange)}
.hero-sub{left:177px;top:318px;font-size:40px;line-height:48px;color:var(--ink);letter-spacing:.5px}
.btn{background:var(--orange);color:var(--white);font-size:34px;text-transform:uppercase;display:flex;align-items:center;justify-content:center;letter-spacing:1px}
.hero-btn{left:187px;top:448px;width:435px;height:58px}
.hero-figure{left:1000px;top:125px;width:110px;height:400px;border-radius:40px;background:linear-gradient(180deg,#e2c0a8,#c9a58d 55%,#9aa3a5)}
.hero-wave{left:0;top:520px}

/* section headings */
.section-title{font-family:"Libre Baskerville",Georgia,serif;font-size:38px;color:var(--ink);letter-spacing:1px}
.section-title em{font-style:normal;color:var(--orange)}
.centered{left:0;width:1200px;text-align:center}

/* about */
.about-title{left:78px;top:770px}
.about-sub{left:78px;top:838px;font-size:30px;color:var(--ink)}
.about-copy{left:78px;top:900px;width:450px;font-size:16px;line-height:21px;color:var(--muted)}
.about-copy p+p{margin-top:21px}
.about-video{left:617px;top:789px;width:506px;height:360px;background:linear-gradient(135deg,#f7a12e,#e67d10 60%,#c96a0c)}
.play{left:805px;top:868px;width:118px;height:118px;border-radius:50%;background:rgba(255,255,255,.55)}

/* services */
.services-title{top:1252px}
.service-img{top:1394px;width:304px;height:324px}
.service-title{top:1734px;width:330px;font-size:20px;font-weight:700;color:var(--ink);letter-spacing:.5px}
.service-copy{top:1774px;width:310px;font-size:17px;line-height:23px;color:var(--muted)}
.services-side{left:0;top:1364px;width:112px;height:466px;background:linear-gradient(180deg,#f5b36b,#f08a2d 50%,#f0c4a0)}
.services-btn{left:388px;top:1924px;width:352px;height:70px}

/* blog */
.blog{left:0;top:2056px;width:1200px;height:757px;background:var(--section-grey)}
.blog-title{top:2080px}
.post-card{top:2208px;width:325px;height:463px;background:var(--white);border:1px solid #f3c690}
.post-img{left:0;top:0;width:100%;height:240px}
.post-title{left:12px;top:268px;font-size:20px;font-weight:700;color:var(--ink);letter-spacing:.5px;white-space:nowrap}
.post-copy{left:12px;top:310px;width:300px;font-size:17px;line-height:23px;color:var(--muted)}
.read-more{left:60px;top:415px;font-size:18px;font-weight:700;color:var(--orange);text-decoration:underline}
.blog-btn{left:363px;top:2721px;width:350px;height:70px}

/* events */
.events-bar{left:72px;top:2823px;width:1066px;height:56px;background:var(--orange);border-left:12px solid #c65f0c}
.events-bar h2{position:absolute;left:22px;top:8px;font-family:"Libre Baskerville",Georgia,serif;font-size:34px;color:var(--white)}
.event-img{top:2920px;width:297px;height:212px;border:1px solid #e6e6e6}
.event-copy{top:3178px;width:290px;font-size:17px;line-height:22px;color:var(--muted)}
.event-date{top:3279px;width:297px;height:50px;display:flex;background:var(--cream);border:1px solid #f3c690}
.event-date span{flex:1;display:flex;align-items:center;justify-content:center;font-size:32px;font-weight:600;color:var(--ink)}
.event-date span+span{border-left:1px solid #f3c690}
.event-label{top:3329px;width:297px;height:40px;background:var(--orange);color:var(--white);font-size:30px;font-weight:700;display:flex;align-items:center;justify-content:center}

/* footer */
.site-footer{left:0;top:3460px;width:1200px;height:274px;background:var(--footer)}
.footer-col{top:3496px;color:var(--footer-text);font-size:13px}
.footer-col h3{font-size:13px;font-weight:700;color:var(--white);margin-bottom:14px;text-transform:uppercase}
.footer-col li{list-style:none;margin-bottom:8px;padding-left:16px;position:relative}
.footer-col li::before{content:"";position:absolute;left:0;top:5px;width:0;height:0;border-left:5px solid var(--footer-text);border-top:4px solid transparent;border-bottom:4px solid transparent}
.footer-divider{left:860px;top:3490px;width:1px;height:150px;background:#333}
.contact-addr{display:flex;gap:10px;line-height:19px}
.footer-map{margin-top:10px;width:150px;height:52px;background:linear-gradient(135deg,#c9d4c1,#9fb5c8)}
.footer-rule{left:72px;top:3660px;width:1056px;height:1px;background:#333}
.copyright{left:125px;top:3680px;font-size:12px;color:var(--footer-text)}
.copyright a{text-decoration:underline;margin:0 8px}
</style>
</head>
<body>

<header class="site-header abs">
  <div class="brand abs"><div class="brand-mark"></div><span class="brand-name">Marlow Hayes</span></div>
  <div class="top-contact abs">
    <span><svg width="20" height="20" viewBox="0 0 20 20"><circle cx="10" cy="10" r="9" fill="none" stroke="#f7941d" stroke-width="2"/><rect x="5" y="6.5" width="10" height="7" fill="none" stroke="#333" stroke-width="1.4"/><path d="M5 6.5l5 4 5-4" fill="none" stroke="#333" stroke-width="1.4"/></svg>Email: hello@marlowhayes.com</span>
    <span><svg width="20" height="20" viewBox="0 0 20 20"><circle cx="10" cy="10" r="9" fill="none" stroke="#f7941d" stroke-width="2"/><path d="M7 5.5l2 2-1 1.5c.8 1.5 1.8 2.5 3 3l1.5-1 2 2-1.5 1.5C9 14 6 11 5.5 7z" fill="#333"/></svg>Phone: 000-000-007</span>
  </div>
  <nav class="main-nav abs">
    <a href="#home">HOME</a><a href="#about">ABOUT ME</a><a href="#services">MY SERVICES</a><a href="#blog">RECENT BLOGS</a><a href="#events">EVENTS</a>
  </nav>
  <div class="search-btn abs"><svg width="20" height="20" viewBox="0 0 20 20"><circle cx="8.5" cy="8.5" r="5.5" fill="none" stroke="#fff" stroke-width="2.4"/><path d="M12.5 12.5l5 5" stroke="#fff" stroke-width="2.6" stroke-linecap="round"/></svg></div>
</header>

<section class="hero abs" id="home"></section>
<h1 class="hero-title abs"><em>Losing</em> Weight</h1>
<p class="hero-sub abs">WITH THE HELP OF A COACH<br>IS DOABLE!</p>
<a class="btn hero-btn abs" href="#about">Make an appoitment</a>
<div class="hero-figure abs" role="img" aria-label="Photo of a slim woman in a bikini top and sarong"></div>
<svg class="hero-wave abs" width="1200" height="90" viewBox="0 0 1200 90"><path d="M0 28 C200 80 420 88 640 54 S1000 -6 1200 22" fill="none" stroke="#f7941d" stroke-width="6"/><path d="M0 40 C220 92 440 96 660 62 S1010 4 1200 34" fill="none" stroke="#fbc98a" stroke-width="3"/></svg>

<section id="about">
  <h2 class="section-title about-title abs">ABOUT <em>ME</em></h2>
  <h3 class="about-sub abs">Ultimate Weight Loss Clinic</h3>
  <div class="about-copy abs">
    <p>If your previous attempts to lose weight have failed, it's not because you failed.</p>
    <p>It's because whatever diets or regimens you tried have failed you. There's no such thing as a one-size-fits-all solution to the weight loss issues. Varying health conditions should also be all taken into account, when tailoring a custom weight loss program for any specific client. In short, we're sure that our extensive experience in helping people to lose that excessive weight will prove to be effective for anyone!</p>
  </div>
  <div class="about-video abs" role="img" aria-label="Video still of people doing step aerobics, tinted orange"></div>
  <svg class="play abs" viewBox="0 0 118 118" role="img" aria-label="Play video"><path d="M46 34 L84 59 L46 84 Z" fill="#f7941d"/></svg>
</section>

<section id="services">
  <h2 class="section-title services-title centered abs">MY <em>SERVICES</em></h2>
  <div class="services-side abs" role="img" aria-label="Photo of a juice glass, tomatoes and a tape measure"></div>
  <div class="service-img abs" style="left:132px;background:linear-gradient(160deg,#dfeccf,#b7d68f 60%,#e46b4f)" role="img" aria-label="Photo of a smiling woman with fresh vegetables and juice"></div>
  <div class="service-img abs" style="left:485px;background:linear-gradient(160deg,#a9d1ec,#d8b49c 55%,#3a3a3a)" role="img" aria-label="Photo of a slim waist with a tape measure"></div>
  <div class="service-img abs" style="left:839px;background:linear-gradient(160deg,#d9b98f,#6b4b36 45%,#e7e3de)" role="img" aria-label="Photo of a hand holding chocolate above bathroom scales"></div>
  <h3 class="service-title abs" style="left:132px">Ultimate Weight Loss Clinic</h3>
  <h3 class="service-title abs" style="left:485px">Health Assessment</h3>
  <h3 class="service-title abs" style="left:839px">Fitness &amp; Activities</h3>
  <p class="service-copy abs" style="left:126px">With no one-fits-it-all diet program existing, we will custom-tailor a dieting program just for you!</p>
  <p class="service-copy abs" style="left:485px">With physical activity being a huge part of one's health and wellbeing, it can help you lose weight too!</p>
  <p class="service-copy abs" style="left:839px">Behind any overweight issue, there's a health problem that's hiding. We want to diagnose and treat it!</p>
  <a class="btn services-btn abs" href="#services">View all services</a>
</section>

<section id="blog">
  <div class="blog abs"></div>
  <h2 class="section-title blog-title centered abs">RECENT <em>BLOGS</em></h2>
  <article class="post-card abs" style="left:72px">
    <div class="post-img abs" style="background:linear-gradient(160deg,#d8d8d8,#a89585 55%,#6b5748)" role="img" aria-label="Photo of a young woman and an older woman together"></div>
    <h3 class="post-title abs">Ultimate Weight Loss Clinic</h3>
    <p class="post-copy abs">With no one-fits-it-all diet program existing, we will custom-tailor a dieting program just for you!</p>
    <a class="read-more abs" href="#blog">Read More</a>
  </article>
  <article class="post-card abs" style="left:433px">
    <div class="post-img abs" style="background:linear-gradient(160deg,#19c3e6,#3fb4d8 55%,#e9e4df)" role="img" aria-label="Photo of a smiling woman giving two thumbs up"></div>
    <h3 class="post-title abs">Ultimate Weight Loss Clinic</h3>
    <p class="post-copy abs">With no one-fits-it-all diet program existing, we will custom-tailor a dieting program just for you!</p>
    <a class="read-more abs" href="#blog">Read More</a>
  </article>
  <article class="post-card abs" style="left:797px">
    <div class="post-img abs" style="background:linear-gradient(160deg,#7f8f6e,#c7b3a0 50%,#e28aa0)" role="img" aria-label="Photo of a woman in sportswear checking her fitness watch"></div>
    <h3 class="post-title abs">Ultimate Weight Loss Clinic</h3>
    <p class="post-copy abs">With no one-fits-it-all diet program existing, we will custom-tailor a dieting program just for you!</p>
    <a class="read-more abs" href="#blog">Read More</a>
  </article>
  <a class="btn blog-btn abs" href="#blog">View all posts</a>
</section>

<section id="events">
  <div class="events-bar abs"><h2>EVENTS</h2></div>
  <div class="event-img abs" style="left:72px;background:linear-gradient(160deg,#e8e8e8,#8d8d8d 55%,#3b3b3b)" role="img" aria-label="Photo of legs doing a step workout"></div>
  <div class="event-img abs" style="left:458px;background:linear-gradient(180deg,#f1f1f1,#d8261c 45%,#6fb13a)" role="img" aria-label="Photo of tomatoes on lettuce with a tape measure"></div>
  <div class="event-img abs" style="left:841px;background:linear-gradient(180deg,#f4f4f4,#2a2a2a 35%,#c99a7c 65%,#f4f4f4)" role="img" aria-label="Photo of a toned woman's torso in a sports top"></div>

  <p class="event-copy abs" style="left:92px">With no one-fits-it-all diet program existing, we will custom-tailor a dieting program just for you!</p>
  <p class="event-copy abs" style="left:468px">With no one-fits-it-all diet program existing, we will custom-tailor a dieting program just for you!</p>
  <p class="event-copy abs" style="left:845px">With no one-fits-it-all diet program existing, we will custom-tailor a dieting program just for you!</p>

  <div class="event-date abs" style="left:72px"><span>31</span><span>OCT</span></div>
  <div class="event-date abs" style="left:458px"><span>05</span><span>NOV</span></div>
  <div class="event-date abs" style="left:841px"><span>10</span><span>DEC</span></div>
  <div class="event-label abs" style="left:72px">Yoga Tips</div>
  <div class="event-label abs" style="left:458px">Health Tips</div>
  <div class="event-label abs" style="left:841px">Fitness Tips</div>
</section>

<footer class="site-footer abs"></footer>
<div class="footer-col abs" style="left:95px"><h3>Quick Link</h3><ul><li>Home</li><li>About Me</li><li>My Services</li><li>Events</li><li>Blog</li></ul></div>
<div class="footer-col abs" style="left:368px"><h3>Information</h3><ul><li>Benefits</li><li>Advices</li><li>Health Report</li><li>Fitness Report</li><li>Mission</li></ul></div>
<div class="footer-col abs" style="left:642px"><h3>Useful Links</h3><ul><li>Booking</li><li>Story</li><li>Location</li><li>Clients</li><li>Why Choose me</li></ul></div>
<div class="footer-divider abs"></div>
<div class="footer-col abs" style="left:914px"><h3>Contact Us</h3>
  <div class="contact-addr"><svg width="14" height="20" viewBox="0 0 14 20"><path d="M7 0a7 7 0 0 0-7 7c0 5 7 13 7 13s7-8 7-13a7 7 0 0 0-7-7z" fill="#cfcfcf"/><circle cx="7" cy="7" r="2.6" fill="#000"/></svg><span>123K, Office Building,<br>Street, City, Country</span></div>
  <div class="footer-map" role="img" aria-label="Small location map"></div>
</div>
<div class="footer-rule abs"></div>
<p class="copyright abs">Copyright © 2017. marlowhayes.com &nbsp;All rights reserved. <a href="#">Terms &amp; Conditions</a>|<a href="#">Privacy Policy</a></p>

</body>
</html>
```